EXTENDED Store hours to serve your healthcare needs

I'M LOOKING FOR A NICE FLYER THAT SHOWS THE FOLLOWING INFORMATION:

Logo
address
tel phone and fax
email address

Extending our hours to meet the growing healthcare needs of our community. Fast delivery service!

Monday - Thursday 10am-midnight
Friday 10am-4pm
Saturday - Motzei Shabbos till midnight
Sunday 10am-7pm

Target Market(s)

Community

Industry/Entity Type

Pharmacy

Requirements
Must have
• Extended hours
• personal care
• expert advice
• superior service
Nice to have
• Looking for no people pictures
• Eye popping design
• Classic modern clean design
Should not have
• store description is services
• And should not say Fiirst to open and last to close

```html
<!DOCTYPE html>
<html lang="en">
<head>
<meta charset="utf-8">
<title>Extended Hours Flyer</title>
<link href="https://fonts.googleapis.com/css2?family=Cabin:ital,wght@0,500;0,600;1,500;1,600&display=swap" rel="stylesheet">
<style>
  :root {
    --page: #ffffff;
    --navy: #1f3a6d;
    --blue: #22579b;
    --blue-deep: #1d4883;
    --yellow: #f5d400;
    --white: #ffffff;
    --tab: #1f3f74;
    --logo-red: #b3242b;
    --logo-blue: #2f55a4;
    --paper: #f4f5f7;
  }
  * { margin: 0; padding: 0; box-sizing: border-box; }
  html, body { width: 1200px; height: 903px; overflow: hidden; background: var(--page); }
  .canvas { position: relative; width: 1200px; height: 903px; overflow: hidden; }
  .stage { position: absolute; left: 0; top: 0; width: 1152px; height: 867px; transform: scale(1.04167); transform-origin: 0 0; }

  .flyer {
    position: absolute; left: 268px; top: 17px; width: 527px; height: 828px;
    background: var(--blue); border: 5px solid var(--navy);
    box-shadow: 2px 3px 6px rgba(0,0,0,.35);
    overflow: hidden; font-family: "Cabin", sans-serif;
  }
  .honeycomb {
    position: absolute; inset: 0;
    background: linear-gradient(160deg, #2661a8 0%, var(--blue) 50%, var(--blue-deep) 100%);
  }
  .title-bar {
    position: absolute; left: 0; top: 0; width: 100%; height: 54px;
    background: var(--navy); color: var(--yellow);
    font-style: italic; font-weight: 600; font-size: 30px;
    display: flex; align-items: center; justify-content: center; letter-spacing: .3px;
  }
  .intro {
    position: absolute; left: 0; top: 70px; width: 100%;
    text-align: center; color: var(--white); font-weight: 600; font-size: 32px; line-height: 40px;
  }
  .hours { position: absolute; left: 0; top: 206px; width: 100%; list-style: none; }
  .hours li { position: relative; height: 40px; margin-bottom: 10px; display: flex; align-items: center; }
  .day {
    height: 40px; display: flex; align-items: center; padding-left: 7px;
    background: var(--tab); border-radius: 0 8px 8px 0;
    color: var(--yellow); font-style: italic; font-weight: 600; font-size: 25px;
    white-space: nowrap;
  }
  .day--wide { width: 272px; }
  .day--short { width: 142px; }
  .time { margin-left: 16px; color: var(--white); font-style: italic; font-weight: 600; font-size: 25px; white-space: nowrap; }
  .hours li:nth-child(1) .time { margin-left: 12px; }

  .contact { position: absolute; top: 423px; color: var(--yellow); font-style: italic; font-size: 21px; line-height: 26.5px; }
  .contact--address { left: 13px; }
  .contact--lines { left: 249px; }

  .wave { position: absolute; left: 0; top: 500px; width: 527px; height: 328px; }

  .brand {
    position: absolute; left: 60px; top: 712px;
    display: flex; align-items: center; gap: 16px;
  }
  .brand-mark { width: 36px; height: 36px; background: var(--logo-blue); }
  .brand-name { color: var(--logo-red); font-weight: 600; font-size: 44px; letter-spacing: .5px; }
</style>
</head>
<body>
<div class="canvas">
  <div class="stage">
    <article class="flyer">
      <div class="honeycomb" role="img" aria-label="Subtle honeycomb pattern in blue tones"></div>

      <header class="title-bar">FAST DELIVERY SERVICE!</header>

      <p class="intro">Extending our hours to meet the<br>growing healthcare<br>needs of our community.</p>

      <ul class="hours">
        <li><span class="day day--wide">MONDAY - THURSDAY</span><span class="time">10am-midnight</span></li>
        <li><span class="day day--short">FRIDAY</span><span class="time">10am-4pm</span></li>
        <li><span class="day day--short">SATURDAY</span><span class="time">Motzei Shabbos till midnight</span></li>
        <li><span class="day day--short">SUNDAY</span><span class="time">10am-7pm</span></li>
      </ul>

      <p class="contact contact--address">Address</p>
      <p class="contact contact--lines">Tel phone<br>Fax<br>email address</p>

      <svg class="wave" viewBox="0 0 527 328" aria-hidden="true">
        <path d="M0 120 C 80 150, 160 50, 260 30 C 360 10, 440 40, 527 60 L527 328 L0 328 Z" fill="var(--navy)"/>
        <path d="M0 205 C 120 110, 300 60, 527 85 L527 328 L0 328 Z" fill="var(--paper)"/>
      </svg>

      <div class="brand">
        <span class="brand-mark"></span>
        <span class="brand-name">Halden Pharmacy</span>
      </div>
    </article>
  </div>
</div>
</body>
</html>
```